Open design - funky concepts for speed dating events website

We are looking for an initial design/concept only (no coding) for 2 pages of an in-development speed dating events website - www.quickmeetmixer.net. Once we have selected a design we will likely then look to engage the winning designer (probably in a freelance project) to complete other areas of the design.

The specification is very open and we're interested to see designs featuring different layouts, colours and design features.

The 2 pages are:
1. Home Page - http://www.quickmeetmixer.net
2. Event Listing Page - http://www.quickmeetmixer.net/Dating-Event.aspx
- the taxonomy section currently on the left hand side may include more items

Both page designs need to include the items that appear on these pages but in no way need to follow the current design or layout - eg. a 'Next Speed Dating Events' section should appear on the home page but where it appears, how many items in the listing, amount of details, size of images etc can change. Other elements may also be added such as image rotators.

Some elements that are on the current website and will appear on all pages:
- social media bookmark links
- ad units - need to include room for advertising locations
- country chooser - events are currently only listed for the UK but the site will eventually be tailored for different countries so users need the ability to select the country site they would like to view

Some elements that aren't on the current website but that should appear:
- User rating system on event listings (eg. 4 out of 5 stars, 1 out of 10, 2 out of 3 'thumbs up')
- User comments/feedback on event listings
- Prominent 'book now' or 'book for this event' type link/button for events (home and events page) and 'visit website' link/button for online listings (home page)

As far as looks we'd like a clean, attractive, personable design. Obviously we'd like some more colour than is currently on the site but we do need users to be able to browse through events and read the details comfortably.

Other than that it's entirely open - we're happy for the designs to be quite funky or less so.
Updates

Some further information following some questions we've received:
- We would like to see all the elements on the current home page in home page designs as fitting it all in is part of the issue. Layout is not set however the priorities for display would be roughly as they are displayed currently. ie. the 'Next Speed Dating Events' section is most prominent, Recently Viewed listings are shown, 'All Upcoming Events' may be below the fold etc.
- We don't have a requirement for a logo on the site and this doesn't necessarily need to appear in designs - totally up to you - we're lookiing at the overall page designs.
- There may be many items in the 'All Upcoming Speed Dating Events' section which we would be including on the home page. Ideally designs would feature a way of displaying these but don't need to include all items

Thank you everyone who submitted to the contest! We had some great designs again and were really impressed with the quality.

Cheers
Gareth

Target Market(s)

Singles looking for speed dating events in their region or online dating websites.

Industry/Entity Type

Advertising

Requirements
Must have
• As in the overview we need the elements that currently appear on the pages.

```html
<!DOCTYPE html>
<html lang="en">
<head>
<meta charset="utf-8">
<title>QuickMeetMixer – Speed Dating Events</title>
<link href="https://fonts.googleapis.com/css2?family=Arimo:wght@400;700&family=Caveat:wght@500&display=swap" rel="stylesheet">
<style>
:root{
  --backdrop:#2a0614;
  --magenta:#9a0d4b;
  --magenta-light:#c0186a;
  --bar-teal:#0e8990;
  --side-teal:#1a9ba2;
  --main-teal:#16a9b0;
  --bright-teal:#20cfd4;
  --foot-teal:#13959c;
  --accent-cyan:#5cf3f6;
  --white:#ffffff;
  --ink:#000000;
  --slate:#8a8a8a;
  --grey-panel:#9d9d9d;
  --btn:#8e0b44;
  --btn-dark:#5a0429;
}
*{box-sizing:border-box;margin:0;padding:0}
html,body{width:960px;height:1200px;overflow:hidden}
body{background:var(--backdrop);font-family:"Arimo",Arial,sans-serif;color:var(--white);position:relative}
.page{position:absolute;left:70px;top:20px;width:820px;height:1160px;background:var(--main-teal);overflow:hidden;box-shadow:0 0 14px rgba(0,0,0,.6)}
.page *{position:absolute}
.page a,.page span{white-space:nowrap}
.header{left:0;top:0;width:820px;height:52px;background:linear-gradient(180deg,var(--magenta-light),var(--magenta))}
.share-tag{left:50px;top:2px;font-family:"Caveat",cursive;font-size:22px;color:var(--accent-cyan)}
.share-arrow{left:14px;top:12px}
.share-icons{left:34px;top:35px;display:flex;gap:6px}
.share-icons i{position:static;display:block;width:20px;height:17px;background:var(--white);border:2px solid #333;border-radius:2px}
.brand{left:560px;top:24px;display:flex;align-items:center;gap:8px}
.brand-dot{position:static;width:16px;height:16px;border-radius:50%;background:var(--ink)}
.brand-name{position:static;font-size:21px;color:var(--white)}
.navbar{left:0;top:52px;width:820px;height:36px;background:linear-gradient(180deg,#16a2a8,var(--bar-teal));border-bottom:1px solid #6fd6da}
.search{left:28px;top:13px;width:146px;height:13px;background:var(--white);color:#9a9a9a;font-size:11px;line-height:13px;text-align:center;font-weight:700;letter-spacing:.5px}
.search-go{left:174px;top:13px;width:16px;height:13px;background:var(--white)}
.nav a,.foot-links a{font-size:10px;letter-spacing:.5px;color:var(--white);text-decoration:none}
.nav a{top:14px}
.sidebar{left:0;top:88px;width:210px;height:802px;background:var(--side-teal);border-right:1px solid #22b4ba}
.side-item{right:630px;font-size:10px;letter-spacing:.5px;text-align:right}
.side-rule{left:0;width:190px;height:3px;background:#0b6f75;border-bottom:1px solid #4fc7cc}
.label{font-size:12.5px;letter-spacing:.5px}
.field{background:var(--white);height:19px;width:96px}
.register{left:105px;top:437px;width:85px;height:19px;background:#137a80;border:1px solid #3db4b9;font-size:10px;letter-spacing:.8px;text-align:center;line-height:17px}
.filter-title{right:630px;font-size:12px;letter-spacing:.8px;text-align:right;white-space:nowrap}
.select{left:35px;width:154px;height:17px;background:var(--white);color:#a5a5a5;font-size:10.5px;font-weight:700;letter-spacing:.5px;line-height:17px;padding-left:20px;overflow:hidden;white-space:nowrap}
.select b{right:0;top:0;width:23px;height:17px;background:#7e7e7e}
.select b::after{content:"";position:absolute;left:5px;top:5px;border-left:6px solid transparent;border-right:6px solid transparent;border-top:8px solid #e0e0e0}
.main-glow{left:210px;top:88px;width:610px;height:802px;background:linear-gradient(180deg,#139da4 0%,var(--main-teal) 35%,var(--bright-teal) 60%,#19b6bc 100%)}
.band{left:211px;width:609px;background:rgba(255,255,255,.05)}
.heading{font-size:13px;font-weight:700;letter-spacing:1.2px;white-space:nowrap}
.slideshow{left:288px;top:147px;width:465px;height:309px;background:#050505;border-radius:10px;border:1px solid #333}
.slide-word{left:0;width:100%;top:110px;text-align:center;font-size:54px;font-weight:700;letter-spacing:3px;color:var(--slate)}
.slide-info{left:10px;top:221px;width:445px;height:54px;background:#3a3a3a;color:#bdbdbd;font-size:12.5px;letter-spacing:.5px}
.slide-info span{right:20px}
.controls{left:205px;top:281px;display:flex;gap:1px}
.controls svg{position:static;display:block}
.btn{background:linear-gradient(180deg,#a9125a,var(--btn));border-radius:5px;box-shadow:0 2px 0 var(--btn-dark);color:var(--white);text-align:center;font-size:10px;letter-spacing:.6px;text-decoration:none}
.view-all{font-size:10px;letter-spacing:1px;color:var(--white);text-decoration:none}
.news-date{left:290px;font-size:14px;font-weight:700;letter-spacing:-.3px}
.news-text{left:420px;width:334px;text-align:right;font-size:9.8px;letter-spacing:-.25px;line-height:13px;white-space:nowrap}
.partner-logo{top:727px;height:40px;background:var(--white);border:1px solid #8fd}
.partner-logo span{left:0;width:100%;top:12px;text-align:center;color:#2b8fd1;font-size:14px;font-weight:700}
.partner-text{font-size:8.3px;line-height:11.3px;white-space:normal}
.footer{left:0;top:890px;width:820px;height:270px;background:var(--foot-teal)}
.ad{left:34px;top:935px;width:752px;height:163px;background:var(--grey-panel);border-radius:3px}
.ad-frame{left:8px;top:6px;width:736px;height:151px;border:3px solid #d9d9d9;border-radius:10px}
.ad-word{left:0;width:100%;top:60px;text-align:center;font-size:32px;font-weight:700;letter-spacing:3px;color:#e4e4e4}
</style>
</head>
<body>
<div class="page">
  <header class="header">
    <svg class="share-arrow" width="22" height="30" viewBox="0 0 22 30"><path d="M18 3 C8 6 6 12 7 24" stroke="#5cf3f6" stroke-width="2.4" fill="none"/><path d="M2 19 L7 27 L12 19" stroke="#5cf3f6" stroke-width="2.4" fill="none"/></svg>
    <span class="share-tag">sharing is sexy!</span>
    <div class="share-icons"><i></i><i></i><i></i><i></i><i></i><i></i></div>
    <div class="brand"><span class="brand-dot"></span><span class="brand-name">QuickMeetMixer</span></div>
  </header>

  <nav class="navbar">
    <div class="search">search site</div>
    <svg class="search-go" width="16" height="13" viewBox="0 0 16 13"><path d="M3 6.5 H10 M8 3 L12 6.5 L8 10" stroke="#555" stroke-width="2" fill="none"/></svg>
    <div class="nav">
      <a style="left:290px">HOME</a>
      <a style="left:341px">ONLINE DATING</a>
      <a style="left:445px">DATING EVENTS</a>
      <a style="left:552px">EVENT PROVIDERS</a>
      <a style="left:673px">EVENT VENUES</a>
    </div>
  </nav>

  <aside class="sidebar"></aside>
  <div class="main-glow"></div>
  <div class="band" style="top:498px;height:195px"></div>
  <div class="band" style="top:693px;height:197px;background:rgba(255,255,255,.03)"></div>

  <span class="side-item" style="top:144px">RECENTLY VIEWED</span>
  <span class="side-item" style="top:164px">Heartlink.com</span>
  <span class="side-item" style="top:178px">Speed Dating Events</span>
  <span class="side-item" style="top:204px">SIMILAR</span>
  <span class="side-item" style="top:224px">Heartlink.com</span>
  <span class="side-item" style="top:238px">Speed dating events</span>
  <span class="side-item" style="top:262px">RSS</span>
  <span class="side-item" style="top:282px">London speed dating</span>
  <span class="side-item" style="top:296px">Birmingham speed dating</span>
  <span class="side-item" style="top:321px">NEWS</span>

  <div class="side-rule" style="top:350px"></div>
  <span class="label" style="left:35px;top:365px">Get Updates</span>
  <span class="label" style="left:35px;top:386px">Location</span>
  <div class="field" style="left:94px;top:383px"></div>
  <span class="label" style="left:35px;top:414px">E-mail</span>
  <div class="field" style="left:94px;top:411px"></div>
  <div class="register">REGISTER</div>
  <div class="side-rule" style="top:490px"></div>

  <div class="filter-title" style="top:505px">ALL UPCOMING</div>
  <div class="filter-title" style="top:523px">SPEED DATING EVENTS</div>
  <div class="filter-title" style="top:544px">LONDON</div>
  <div class="select" style="top:560px;padding-left:33px">Choose venue....<b></b></div>
  <div class="filter-title" style="top:593px">OUTSIDE LONDON</div>
  <div class="select" style="top:609px;padding-left:33px">Choose venue....<b></b></div>
  <div class="filter-title" style="top:642px">BY DATE</div>
  <div class="select" style="top:658px;padding-left:42px">Choose date....<b></b></div>
  <div class="filter-title" style="top:691px">BY CATEGORY</div>
  <div class="select" style="top:707px">Choose category....<b></b></div>
  <div class="filter-title" style="top:740px">BY EVENT PROVIDER</div>
  <div class="select" style="top:756px">Choose provider....<b></b></div>

  <h2 class="heading" style="left:290px;top:128px">SPEED DATING EVENTS COMING UP</h2>
  <section class="slideshow" role="img" aria-label="Rotating photos of upcoming speed dating events">
    <div class="slide-word">SLIDESHOW</div>
    <div class="slide-info"><span style="top:4px">Info about the event,venue and other details..</span><span style="top:37px;font-weight:700">more..</span></div>
    <div class="controls">
      <svg width="17" height="22" viewBox="0 0 17 22"><rect width="17" height="22" fill="#4f8f92"/><path d="M13 4 L4 11 L13 18Z" fill="#bfe"/></svg>
      <svg width="17" height="22" viewBox="0 0 17 22"><rect width="17" height="22" fill="#4f8f92"/><rect x="4" y="4" width="3" height="14" fill="#bfe"/><rect x="10" y="4" width="3" height="14" fill="#bfe"/></svg>
      <svg width="17" height="22" viewBox="0 0 17 22"><rect width="17" height="22" fill="#4f8f92"/><path d="M4 4 L13 11 L4 18Z" fill="#bfe"/></svg>
    </div>
  </section>
  <a class="btn" style="left:303px;top:460px;width:177px;height:21px;line-height:21px">BOOK NOW!</a>
  <a class="btn" style="left:576px;top:460px;width:177px;height:21px;line-height:21px">VIEW ALL UPCOMING EVENTS</a>

  <h2 class="heading" style="left:290px;top:505px">DATING NEWS</h2>
  <a class="view-all" style="left:688px;top:509px">VIEW ALL..</a>
  <span class="news-date" style="top:528px">Sunday 03 October</span>
  <p class="news-text" style="top:531px">Dating news story summary covering a few lines of the text of the article<br>with a link to the rest of the story so the user can view the full article...<br>Read full article</p>
  <span class="news-date" style="top:572px">Sunday 03 October</span>
  <p class="news-text" style="top:575px">Dating news story summary covering a few lines of the text of the article<br>with a link to the rest of the story so the user can view the full article...<br>Read full article</p>
  <span class="news-date" style="top:617px">Sunday 03 October</span>
  <p class="news-text" style="top:620px">Dating news story summary covering a few lines of the text of the article<br>with a link to the rest of the story so the user can view the full article...<br>Read full article</p>

  <h2 class="heading" style="left:290px;top:706px">ONLINE DATING WEBSITES</h2>
  <a class="view-all" style="left:688px;top:709px">VIEW ALL..</a>
  <div class="partner-logo" style="left:288px;width:146px"><span>Pairwise</span></div>
  <div class="partner-logo" style="left:488px;width:78px"><span style="font-size:11px;top:13px">Spark &amp; Chat</span></div>
  <div class="partner-logo" style="left:641px;width:84px"><span style="font-size:10px;top:13px">Kinfolk Singles</span></div>
  <p class="partner-text" style="left:287px;top:774px;width:140px">Pairwise is a premium dating and events organisation for professionals.</p>
  <p class="partner-text" style="left:455px;top:774px;width:148px">Spark &amp; Chat is an International casual dating site where everyone can make new friends, communicate and find a date. A place where people from all over the globe flirt non-stop!</p>
  <p class="partner-text" style="left:615px;top:772px;width:145px">Kinfolk Singles is the premier Jewish singles community online. Kinfolk has been building the Jewish community for more than a decade, so it's not surprising that it seems like everyone knows someone who fell in love on Kinfolk and it's no wonder why countless marriages begin right here!</p>
  <a class="btn" style="left:291px;top:867px;width:130px;height:17px;line-height:17px;font-size:9.5px">visit website</a>
  <a class="btn" style="left:455px;top:867px;width:130px;height:17px;line-height:17px;font-size:9.5px">visit website</a>
  <a class="btn" style="left:617px;top:867px;width:130px;height:17px;line-height:17px;font-size:9.5px">visit website</a>

  <footer class="footer"></footer>
  <div class="foot-links">
    <a style="left:279px;top:900px">HOME</a>
    <a style="left:330px;top:900px">ONLINE DATING</a>
    <a style="left:434px;top:900px">DATING EVENTS</a>
    <a style="left:541px;top:900px">EVENT PROVIDERS</a>
    <a style="left:662px;top:900px">EVENT VENUES</a>
  </div>
  <div class="ad" role="img" aria-label="Advertisement space">
    <div class="ad-frame"></div>
    <div class="ad-word">ADVERTISEMENT SPACE</div>
  </div>
  <div class="foot-links">
    <a style="left:330px;top:1131px">CONTACT US</a>
    <span style="left:415px;top:1130px;width:2px;height:11px;background:#fff"></span>
    <a style="left:434px;top:1131px">ABOUT US</a>
  </div>
</div>
</body>
</html>
```